We need a brand new Employee Handbook for a team of aged and disability support workers

We need an employee handbook designed for our team of aged and disability support workers.
We provide a range of disability and aged care services to persons in our region.
We are a small business, providing unique and personalised support to vulnerable people. We actually provide choice and control to our clients - something the bigger agencies say they do but don't follow through with.
We aim to be an employer of choice - providing a workplace that supports our staff personally and professionally.
We would like to see the colours gold, yellow, black, grey and white.
We would like to incorporate photos of our current team members and stock photos of fun teams, persons with a disability, elderly and carers in the community and home.
The final design should communicate a fun, supportive team offering growth and opportunity.

```html
<!DOCTYPE html>
<html lang="en">
<head>
<meta charset="utf-8">
<title>Marlowe Care – Induction Guide</title>
<link href="https://fonts.googleapis.com/css2?family=Inter:wght@400;500;600;700;800&display=swap" rel="stylesheet">
<style>
  :root{
    --gold-dark:#b8982f;
    --gold:#d1b44a;
    --gold-light:#ecd878;
    --gold-text:#b39630;
    --ink:#111111;
    --grey:#8a8a8a;
    --grey-mid:#7d7d7d;
    --white:#ffffff;
    --shadow:0 2px 10px rgba(0,0,0,.18);
  }
  *{margin:0;padding:0;box-sizing:border-box}
  html,body{width:926px;height:1200px;overflow:hidden;background:var(--white)}
  body{position:relative;font-family:"Inter",Arial,sans-serif;color:var(--ink)}
  .page{position:absolute;width:375px;height:290px;background:var(--white);box-shadow:var(--shadow);overflow:hidden}
  .page--cover{left:67px;top:111px}
  .page--welcome{left:483px;top:111px}
  .page--contents{left:67px;top:460px}
  .page--pledge{left:483px;top:460px}
  .page--director{left:255px;top:808px}
  .abs{position:absolute}
  .gold-pill{position:absolute;border-radius:20px;background:linear-gradient(180deg,var(--gold-light),var(--gold) 55%,var(--gold-dark));box-shadow:0 1px 2px rgba(0,0,0,.25)}
  .photo{position:absolute}

  /* cover */
  .cover-photo{left:173px;top:0;width:202px;height:290px;background:linear-gradient(150deg,#cfd8e6 0%,#e6b9a3 40%,#d98d80 65%,#8c9bb0 100%)}
  .cover-title-panel{left:173px;top:88px;width:51px;height:93px;background:var(--white)}
  .brand{left:28px;top:40px;font-size:15px;font-weight:700;color:var(--gold-text);letter-spacing:.2px}
  .cover-title{left:24px;top:95px;font-size:43px;line-height:40px;font-weight:700;letter-spacing:-1px}
  .cover-pill{left:27px;top:223px;width:134px;height:26px;display:flex;align-items:center;padding-left:14px}
  .cover-pill span{font-size:6.5px;line-height:8px;font-weight:500;width:80px}
  .cover-pill svg{position:absolute;right:12px;top:10px}

  /* welcome */
  .welcome-title{left:26px;top:108px;font-size:37px;font-weight:700;letter-spacing:-1px}
  .welcome-pill{left:26px;top:150px;width:170px;height:19px;display:flex;align-items:center;justify-content:center;font-size:7.3px;font-weight:500}
  .welcome-photo{left:225px;top:77px;width:126px;height:126px;border-radius:50%;background:radial-gradient(circle at 50% 35%,#bfe7f5 0%,#4cc1e6 45%,#3f8d3f 85%)}
  .acknowledgement{left:26px;top:253px;font-size:4.4px;font-weight:500;white-space:nowrap}

  /* contents */
  .contents-photo{left:0;top:0;width:180px;height:290px;background:linear-gradient(135deg,#3a3a3a 0%,#d7d7d7 35%,#8a5a3a 60%,#b7b7b7 100%)}
  .contents-title{left:201px;top:54px;color:var(--grey);font-weight:500;letter-spacing:-.5px}
  .contents-title .small{display:block;font-size:19px;line-height:19px}
  .contents-title .large{display:block;font-size:30px;line-height:28px;font-weight:600}
  .contents-rule{left:201px;top:110px;width:36px;height:3px;background:#555}
  .contents-list{left:207px;top:122px;list-style:none;font-size:5.6px;font-weight:500}
  .contents-list li{height:9.5px;display:flex}
  .contents-list li b{font-weight:500;width:12px}
  .contents-sub{list-style:none;margin-left:12px;font-size:4.4px;font-weight:600}
  .contents-sub li{height:6.1px}

  /* pledge */
  .pledge-photo{left:199px;top:0;width:176px;height:290px;background:linear-gradient(160deg,#e6c9a8 0%,#c4a07c 35%,#7a8aa0 70%,#d9dde2 100%)}
  .pledge-heading{left:28px;top:38px;font-size:15.5px;line-height:19px;font-weight:400;white-space:nowrap}
  .pledge-heading strong{font-weight:800;color:#151a2e}
  .pledge-body{left:27px;top:88px;font-size:5.4px;line-height:6.8px;font-weight:600;white-space:nowrap}
  .pledge-body p{margin-bottom:6.8px}
  .footer-bar{position:absolute;height:9px;background:var(--grey-mid);color:var(--white);font-size:5px;line-height:9px;padding-left:5px}
  .page-num{position:absolute;height:9px;background:var(--grey-mid);color:var(--white);font-size:5px;line-height:9px;text-align:center}
  .pledge-footer{left:26px;top:260px;width:320px}
  .pledge-num{left:348px;top:260px;width:22px}

  /* director */
  .director-photo{left:27px;top:50px;width:103px;height:136px;border:2px solid #e6e6e6;background:linear-gradient(180deg,#cfcfcf,#6e6e6e);box-shadow:0 1px 3px rgba(0,0,0,.3)}
  .director-pill{left:27px;top:199px;width:103px;height:17px;display:flex;align-items:center;justify-content:center;font-size:6.5px;font-weight:500}
  .director-role{left:27px;top:226px;width:103px;text-align:center;font-size:5.4px;line-height:6.8px}
  .director-heading{left:164px;top:46px;font-size:19.5px;line-height:23px;font-weight:800;color:var(--gold-text);white-space:nowrap}
  .director-lead{left:164px;top:99px;font-size:9.1px;line-height:11.4px;font-weight:400;letter-spacing:-.2px;white-space:nowrap}
  .director-body{left:164px;top:178px;font-size:5px;line-height:6.9px;font-weight:500;letter-spacing:-.05px;white-space:nowrap}
  .director-sign{left:164px;top:233px;font-size:6.5px}
  .director-footer{left:27px;top:259px;width:318px}
  .director-num{left:349px;top:259px;width:26px}
</style>
</head>
<body>

<section class="page page--cover">
  <div class="photo cover-photo" role="img" aria-label="Photo of team members stacking hands together"></div>
  <div class="abs cover-title-panel"></div>
  <div class="abs brand">Marlowe Care</div>
  <h1 class="abs cover-title">Induction<br>Guide</h1>
  <div class="gold-pill cover-pill">
    <span>A practical guide to your employment journey</span>
    <svg width="28" height="6" viewBox="0 0 28 6"><path d="M0 3H26M22 0.5L26.5 3L22 5.5" stroke="#111" stroke-width="0.9" fill="none"/></svg>
  </div>
</section>

<section class="page page--welcome">
  <h2 class="abs welcome-title">Welcome!</h2>
  <div class="gold-pill welcome-pill">WE'RE GLAD TO HAVE YOU ON BOARD.</div>
  <div class="photo welcome-photo" role="img" aria-label="Photo of a smiling older man in a green jumper giving an OK sign"></div>
  <p class="abs acknowledgement">We acknowledge the traditional owners of the land we work on - the Ngunnawal people - and pay our respect to their Elders both past and present</p>
</section>

<section class="page page--contents">
  <div class="photo contents-photo" role="img" aria-label="Photo of two colleagues working together at a laptop"></div>
  <h2 class="abs contents-title"><span class="small">TABLE OF</span><span class="large">CONTENT</span></h2>
  <div class="abs contents-rule"></div>
  <ol class="abs contents-list">
    <li><b>01.</b>EMPLOYER PLEDGE</li>
    <li><b>02.</b>MESSAGE FROM DIRECTOR</li>
    <li><b>03.</b>INTRODUCTION</li>
    <li><b>04.</b>OUR STORY</li>
    <li><b>05.</b>OUR MISSION</li>
    <li><b>06.</b>OUR VALUES</li>
    <li style="height:7px"><b>07.</b>OUR GOALS</li>
    <li style="height:auto">
      <ul class="contents-sub">
        <li>a) HIERARCHICAL STRUCTURE</li>
        <li>b) OUR TEAM</li>
        <li>c) YOUR ROLE</li>
        <li>d) YOUR QUALITIES</li>
        <li>e) YOUR TRAINING PLAN</li>
        <li>f) YOUR COACH</li>
        <li>g) YOUR RGHTS &amp;</li>
        <li>h) RESPONSIBILITIES</li>
        <li>i) ONBOARDING CHECKLIST</li>
        <li>j) SYSTEMS &amp; TOOLS</li>
      </ul>
    </li>
  </ol>
</section>

<section class="page page--pledge">
  <div class="photo pledge-photo" role="img" aria-label="Photo of a young man working on a laptop in an office"></div>
  <h2 class="abs pledge-heading">Our pledge to be an<br><strong>'Employer of Choice'</strong></h2>
  <div class="abs pledge-body">
    <p>We care about you! You matter.<br>Your family and those who care for you,<br>matter.</p>
    <p>Your emotional, physical, spiritual and<br>psychological needs are important to us.<br>Giving you opportunity for professional and<br>personal growth is important to us.</p>
    <p>Giving you opportunity for training, skill<br>development and career progression is<br>important to us.</p>
    <p>We will listen to you. We will give you<br>constructive feedback.</p>
    <p>We will support you based on your needs<br>and goals.</p>
    <p>Your wellbeing inspires us to grow, learn and<br>improve.</p>
  </div>
  <div class="footer-bar pledge-footer">www.marlowecare.example</div>
  <div class="page-num pledge-num">03</div>
</section>

<section class="page page--director">
  <div class="photo director-photo" role="img" aria-label="Black and white portrait of the director"></div>
  <div class="gold-pill director-pill">JO HARLAN</div>
  <p class="abs director-role">Director<br>Marlowe Care</p>
  <h2 class="abs director-heading">Message from the<br>Director</h2>
  <p class="abs director-lead">Welcome to Marlowe Care!<br>We are thrilled to have you join our team.<br>We do some amazing, exciting &amp; challenging<br>work here, and we are hopeful that your<br>talent, enthusiasm, and fresh ideas will help<br>take us to a new level!</p>
  <p class="abs director-body">We hope that you find this handbook useful. We welcome any suggestions<br>and comments you may have - please don't hesitate to ask any questions.<br>I'm sure you will find your role challenging but rewarding; as we conti-<br>nuously make a positive difference to our clients lives, in our everyday<br>transactions. We look forward to you contributing to our commitment to<br>place participant choice and control at the forefront of everything we do.<br>We hope you enjoy this journey as much as we will!</p>
  <p class="abs director-sign">- Jo</p>
  <div class="footer-bar director-footer">www.marlowecare.example</div>
  <div class="page-num director-num">04</div>
</section>

</body>
</html>
```